Marrowind Booking Engine Marketing Site

Hi,
I’m currently in the process of putting together a web application with the intention of providing small resorts/B&Bs/small hotels the ability to allow their customers to book online.
I’m looking to have a design created for a marketing site, to give potential customers additional information about my booking engine, as well as to help drive sign-ups. A lot of the competition out there appears outdated, so I would like something that is more modern and up to date.
I am looking for just the design (i’m a web developer, but I lack the creative skills for a good marketing site)
For some more background, I will be targeting business owners of smaller resorts and Bed & Breakfasts. These are typically family owned small businesses that may only have a 10 room setup. These businesses will also typically have additional amenities that they will have to rent out or sell to their clients ( ex. Spa, fruit basket, water sport rentals). My software will provide them with the ability to sell their amenities as well.
I’m open to different designs, but my main thing is I want it to look modern, and I want it to have several callouts to sign up for my product.
I am looking to have the homepage created, 1 interior page, and a style guide created (to show form fields, H1’s, etc.).
I had a logo created a couple months ago that will be included with this project brief.
If you need any additional information feel free to reach out to me.

Target Market(s)

This site will be targeted small business owners who are running small resorts, Bed and Breakfasts, or any business that provides rooms for their clients.

Industry/Entity Type

Saas

Number of Pages Required

2 page

Font styles to use
Sans Serif

Colors

Designer to choose colors to be used in the design.

Requirements
Must have
• A modern feel, with several CTA's that will drive to the registration page on the homepage. on the internal page, I mostly just need the page layout, I will reuse that page layout. and a style guide if at all possible (include colors, form fields, H1's, etc.)
Nice to have
• maybe a hero image at the top with buttons over the top? again i'm pretty open to most anything.
Should not have
• I like images, but I don't want the page overrun with images. A good balance.

```html
<!DOCTYPE html>
<html lang="en">
<head>
<meta charset="utf-8">
<title>Marrowind Booking Engine – Style Guide</title>
<link href="https://fonts.googleapis.com/css2?family=Montserrat:wght@300;400;500;600;700&family=Nunito:wght@800;900&display=swap" rel="stylesheet">
<style>
  :root{
    --ink:#282828;
    --graphite:#5a5a5a;
    --mist:#efefef;
    --teal:#40c1ca;
    --coral:#fe562e;
    --navy:#004b80;
    --blue:#1186fc;
    --sky:#4fb5f7;
    --green:#81bf00;
    --page:#eef1f5;
    --rule:#d8dde4;
    --muted:#8793a8;
    --heading:#5f6f88;
    --icon:#2d3a6b;
    --marker:#e0198a;
  }
  *{box-sizing:border-box;margin:0;padding:0}
  html,body{width:814px;height:1200px;overflow:hidden}
  body{font-family:"Montserrat",sans-serif;background:var(--page);position:relative;color:var(--muted)}
  .abs{position:absolute}

  .masthead{position:absolute;left:0;top:0;width:814px;height:140px;background:#fff}
  .brand{position:absolute;left:38px;top:56px;display:flex;align-items:center;gap:8px}
  .brand-dot{width:26px;height:26px;border-radius:50%;background:var(--green)}
  .brand-name{font-size:15px;font-weight:500;color:var(--navy);line-height:1.15}
  .masthead-title{position:absolute;left:228px;top:60px;font-size:19px;font-weight:600;color:#8a94a6}

  .section-title{position:absolute;font-size:18px;font-weight:400;color:var(--heading);letter-spacing:.2px}
  .section-title small{font-size:10px;margin-right:4px}
  .rule{position:absolute;height:1px;background:var(--rule)}

  .swatch{position:absolute;top:227px;width:73px;height:109px;background:#fff;box-shadow:0 3px 6px rgba(0,0,0,.12)}
  .swatch .chip{height:73px;display:flex}
  .swatch .chip span{flex:1}
  .swatch .code{height:36px;display:flex;flex-direction:column;align-items:center;justify-content:center;font-size:10px;color:var(--ink);line-height:1.4}

  .family{position:absolute;left:34px;top:430px;font-size:60px;font-weight:300;color:#7e8ba0;letter-spacing:.5px}
  .type-row{position:absolute;left:36px;display:flex;color:var(--muted)}
  .type-row span:first-child{width:141px}
  .t-title{top:514px;font-size:29px;font-weight:300}
  .t-title span:first-child{margin-left:-4px;width:145px}
  .t-sub{top:557px;font-size:23px}
  .t-menu{top:591px;font-size:13px;font-weight:700}
  .t-body{top:620px;font-size:13px}
  .t-para{top:649px;font-size:13px}

  .lh-label{position:absolute;left:418px;top:479px;font-size:10px;color:var(--ink)}
  .demo-h1{position:absolute;left:418px;top:534px;font-size:36px;font-weight:600;color:var(--navy)}
  .demo-h2{position:absolute;left:418px;top:579px;font-size:21px;font-weight:500;color:var(--blue)}
  .demo-p{position:absolute;left:418px;font-size:13px;font-weight:500;color:var(--muted)}
  .marker{position:absolute;font-size:9px;color:var(--marker)}
  .marker-line{position:absolute;left:419px;width:1px;background:var(--marker)}

  .caption{position:absolute;font-size:10px;color:var(--graphite)}
  .btn{position:absolute;width:159px;height:41px;border-radius:21px;font-family:"Nunito",sans-serif;font-weight:900;font-size:14px;display:flex;align-items:center;justify-content:center}
  .btn-primary{background:var(--blue);color:#fff}
  .btn-light{background:#fff;color:var(--blue)}
  .btn-hover{box-shadow:0 8px 14px rgba(40,60,90,.22)}

  .nav{position:absolute;left:420px;top:828px;display:flex;gap:18px;font-size:13px;font-weight:600;color:#4a5568}
  .nav .active{color:var(--navy);position:relative}
  .nav .active::after{content:"";position:absolute;left:0;right:-2px;top:27px;height:2px;background:var(--navy)}

  .icon{position:absolute;width:44px;height:44px;display:flex;align-items:center;justify-content:center}
  .social{position:absolute;font-size:11px;font-weight:600;color:#8a94a6;width:80px;text-align:center}
</style>
</head>
<body>

<header class="masthead">
  <div class="brand"><span class="brand-dot"></span><span class="brand-name">Marrowind<br>Booking Engine</span></div>
  <div class="masthead-title">Style Guide</div>
</header>

<!-- Colour palette -->
<div class="section-title" style="left:36px;top:164px"><small>01.</small>COLOUR PALETTE</div>
<div class="rule" style="left:36px;top:196px;width:742px"></div>

<div class="swatch" style="left:36px"><div class="chip"><span style="background:var(--ink)"></span></div><div class="code">#282828</div></div>
<div class="swatch" style="left:131px"><div class="chip"><span style="background:var(--graphite)"></span></div><div class="code">#5A5A5A</div></div>
<div class="swatch" style="left:226px"><div class="chip"><span style="background:var(--mist)"></span></div><div class="code">#EFEFEF</div></div>
<div class="swatch" style="left:322px"><div class="chip"><span style="background:var(--teal)"></span></div><div class="code">#40C1CA</div></div>
<div class="swatch" style="left:418px"><div class="chip"><span style="background:var(--coral)"></span></div><div class="code">#FE562E</div></div>
<div class="swatch" style="left:513px"><div class="chip"><span style="background:var(--navy)"></span></div><div class="code">#004B80</div></div>
<div class="swatch" style="left:609px"><div class="chip"><span style="background:var(--blue)"></span><span style="background:var(--sky)"></span></div><div class="code">#1186FC<span>#4FB5F7</span></div></div>
<div class="swatch" style="left:704px"><div class="chip"><span style="background:var(--green)"></span></div><div class="code">#81BF00</div></div>

<!-- Typography -->
<div class="section-title" style="left:36px;top:390px"><small>02.</small>TYPOGRAPHY</div>
<div class="rule" style="left:36px;top:423px;width:742px"></div>

<div class="family">Montserrat</div>
<div class="type-row t-title"><span>Title</span><span>Light 40px</span></div>
<div class="type-row t-sub"><span>Subheader</span><span>Regular 30px</span></div>
<div class="type-row t-menu"><span>Menu/Button</span><span>Bold 18px</span></div>
<div class="type-row t-body"><span>Body 1</span><span>Regular 18px</span></div>
<div class="type-row t-para"><span>Paragraph</span><span>Regular 18px</span></div>

<div class="lh-label">LINE HEIGHT</div>
<div class="demo-h1">Marrowind Booking</div>
<div class="marker" style="left:390px;top:568px">20 px</div>
<div class="marker-line" style="top:566px;height:16px"></div>
<div class="demo-h2">Manage Hotel or BnB</div>
<div class="marker" style="left:390px;top:609px">40 px</div>
<div class="marker-line" style="top:606px;height:18px"></div>
<div class="demo-p" style="top:625px">Marrowind Booking Engine is a online booking service.</div>
<div class="demo-p" style="top:666px">It's a centralised platform where service providers can</div>
<div class="demo-p" style="top:693px">manage various aspects of their business with</div>

<!-- Buttons & navigation -->
<div class="section-title" style="left:36px;top:726px"><small>03.</small>BUTTONS</div>
<div class="section-title" style="left:418px;top:726px"><small>04.</small>NAVIGATION</div>
<div class="rule" style="left:36px;top:759px;width:742px"></div>

<div class="caption" style="left:36px;top:787px">FILLED BUTTONS</div>
<div class="caption" style="left:36px;top:824px">Normal</div>
<div class="caption" style="left:227px;top:824px">Normal</div>
<div class="btn btn-primary" style="left:36px;top:839px">Join Marrowind</div>
<div class="btn btn-light" style="left:227px;top:839px">Join Marrowind</div>
<div class="caption" style="left:36px;top:888px">Hover</div>
<div class="caption" style="left:227px;top:888px">Hover</div>
<div class="btn btn-primary btn-hover" style="left:36px;top:905px">Join Marrowind</div>
<div class="btn btn-light btn-hover" style="left:227px;top:905px">Join Marrowind</div>

<nav class="nav"><span class="active">About</span><span>How it Works</span><span>Plans</span></nav>

<!-- Icons -->
<div class="section-title" style="left:36px;top:992px"><small>05.</small>ICONS</div>
<div class="rule" style="left:36px;top:1025px;width:742px"></div>

<div class="icon" style="left:30px;top:1047px"><svg width="38" height="38" viewBox="0 0 38 38"><circle cx="19" cy="19" r="17" fill="none" stroke="var(--green)" stroke-width="2.5"/><path d="M11 19l6 6 10-11" fill="none" stroke="var(--green)" stroke-width="2.5" stroke-linecap="round" stroke-linejoin="round"/></svg></div>
<div class="icon" style="left:135px;top:1047px"><svg width="40" height="40" viewBox="0 0 40 40" fill="none" stroke="var(--icon)" stroke-width="1.8"><path d="M15 3c-2 2 2 3 0 6M21 3c-2 2 2 3 0 6"/><path d="M9 14h20v10a8 8 0 0 1-8 8h-4a8 8 0 0 1-8-8z"/><path d="M29 17h3a3 3 0 0 1 0 6h-3"/><circle cx="19" cy="22" r="3" fill="#7b5cf0"/><path d="M4 36h30"/></svg></div>
<div class="icon" style="left:248px;top:1047px"><svg width="42" height="40" viewBox="0 0 42 40" fill="none" stroke="var(--icon)" stroke-width="1.8"><rect x="2" y="2" width="38" height="28" rx="2"/><path d="M2 25h38" stroke="var(--teal)" stroke-width="4"/><path d="M21 30v6M14 37h14"/></svg></div>
<div class="icon" style="left:360px;top:1047px"><svg width="30" height="40" viewBox="0 0 30 40" fill="none" stroke="var(--icon)" stroke-width="1.8"><path d="M3 2l4 3 4-3 4 3 4-3 4 3 4-3v34l-4-3-4 3-4-3-4 3-4-3-4 3z"/><path d="M8 12h14M8 17h10M8 22h8" stroke="var(--teal)"/><path d="M20 22v10" stroke="#7b5cf0"/></svg></div>
<div class="icon" style="left:472px;top:1047px"><svg width="40" height="40" viewBox="0 0 40 40" fill="none" stroke="var(--icon)" stroke-width="1.8"><path d="M8 2h18l8 8v26H8z"/><path d="M26 2v8h8" fill="var(--green)"/><path d="M3 8v30h25"/><path d="M13 16h16M13 21h16M13 26h12M13 31h10"/></svg></div>
<div class="icon" style="left:584px;top:1047px"><svg width="36" height="36" viewBox="0 0 36 36" stroke="var(--icon)" stroke-width="1.8"><rect x="2" y="3" width="32" height="12" rx="6" fill="none"/><circle cx="9" cy="9" r="6" fill="#7b5cf0"/><rect x="2" y="21" width="32" height="12" rx="6" fill="#8ec7e8"/><circle cx="27" cy="27" r="6" fill="var(--teal)"/></svg></div>
<div class="icon" style="left:697px;top:1047px"><svg width="42" height="40" viewBox="0 0 42 40" fill="none" stroke="var(--icon)" stroke-width="1.8"><path d="M2 18L21 3l19 15"/><path d="M7 15v22h28V15"/><rect x="18" y="25" width="7" height="12" fill="var(--teal)"/><path d="M29 5v6" stroke="#7b5cf0" stroke-width="3"/></svg></div>

<div class="icon" style="left:30px;top:1108px"><svg width="38" height="40" viewBox="0 0 38 40" fill="#8a94a6"><path d="M19 2a3 3 0 0 1 3 3" fill="none" stroke="#8a94a6" stroke-width="1.6"/><path d="M19 6L2 16h34z" fill="none" stroke="#8a94a6" stroke-width="1.6"/><rect x="6" y="16" width="26" height="20"/><path d="M6 38h26" stroke="#8a94a6" stroke-width="2" stroke-dasharray="1 1.5"/></svg></div>
<div class="icon" style="left:135px;top:1108px"><svg width="40" height="30" viewBox="0 0 40 30" fill="#8a94a6"><rect x="2" y="4" width="3" height="24"/><rect x="35" y="14" width="3" height="14"/><rect x="2" y="18" width="36" height="5"/><rect x="7" y="11" width="8" height="6" rx="2"/><rect x="16" y="12" width="19" height="6" rx="2"/></svg></div>
<div class="icon" style="left:248px;top:1108px"><svg width="44" height="40" viewBox="0 0 44 40" fill="#8a94a6"><path d="M10 4h24v32H10z"/><rect x="13" y="9" width="18" height="14" fill="#fff"/><path d="M13 16h18M19 9v14M25 9v14" stroke="#8a94a6" stroke-width="1.5"/><rect x="4" y="22" width="7" height="14"/><rect x="33" y="22" width="7" height="14"/><rect x="2" y="37" width="40" height="2"/></svg></div>
<div class="icon" style="left:360px;top:1108px"><svg width="36" height="36" viewBox="0 0 36 36"><circle cx="18" cy="18" r="18" fill="var(--blue)"/><path d="M11 15l7 7 7-7" fill="none" stroke="#fff" stroke-width="2.5" stroke-linecap="round" stroke-linejoin="round"/></svg></div>
<div class="social" style="left:454px;top:1124px">Chirper</div>
<div class="social" style="left:566px;top:1124px">Friendbook</div>
<div class="social" style="left:679px;top:1124px">Circlenet</div>

</body>
</html>
```